Advertisement for linkora Ad

We are looking to copy a mailer style design that would normally be sent out to a mailbox. However we have decided to simply use it and run an add on Linkora. please check photo sizes for linkora to make sure your design will work.

also please try to use the colors from our website: brightmeadowclub@postvane.net

we want the same layout as the ad we sent in the files, with different photos and color scheme.

Target Market(s)

dog owners with busy schedules

Font styles to use
Sans Serif

Colors

Designer to choose only greyscale colors for use in the design.

```html
<!DOCTYPE html>
<html lang="en">
<head>
<meta charset="utf-8">
<title>Bright Meadow Club – Dog Day Care</title>
<link rel="stylesheet" href="https://fonts.googleapis.com/css2?family=Roboto:wght@400;500;700;900&display=swap">
<style>
  :root {
    --photo-dark: #2f2f2f;
    --photo-mid: #6e6e6e;
    --photo-light: #a9a9a9;
    --panel-1: #ededed;
    --panel-2: #cfcfcf;
    --strip-1: #f4f4f4;
    --strip-2: #e4e4e4;
    --headline: #262626;
    --ink: #161616;
    --paw: #4a4a4a;
    --band: #8c8c8c;
    --footer: #2c2c2c;
    --white: #ffffff;
    --offer-dark: #1f1f1f;
    --offer-mid: #4d4d4d;
    --offer-deep: #363636;
    --ring: #b5b5b5;
  }
  * { margin: 0; padding: 0; box-sizing: border-box; }
  html, body { width: 1200px; height: 628px; overflow: hidden; background: var(--white); }
  .ad {
    position: relative; width: 1200px; height: 628px; overflow: hidden;
    font-family: "Roboto", Arial, sans-serif; color: var(--ink);
  }
  .hero-photo {
    position: absolute; left: 0; top: 0; width: 1200px; height: 390px;
    background: linear-gradient(120deg, var(--photo-dark) 0%, var(--photo-mid) 35%, var(--photo-light) 55%, var(--photo-mid) 75%, var(--photo-dark) 100%);
  }
  .panel-shape { position: absolute; left: 0; top: 0; width: 1200px; height: 390px; }
  .headline { position: absolute; left: 619px; top: 22px; color: var(--headline); font-weight: 400; }
  .headline-kicker { font-size: 27px; line-height: 32px; letter-spacing: 0.6px; }
  .headline-main { font-size: 50px; line-height: 56px; letter-spacing: 0.3px; }
  .features { position: absolute; left: 598px; top: 116px; list-style: none; }
  .features li {
    position: relative; padding-left: 22px; font-size: 17px; font-weight: 500;
    line-height: 20px; margin-bottom: 10px; letter-spacing: 0.4px;
  }
  .features li::before {
    content: ""; position: absolute; left: 2px; top: 4px; width: 12px; height: 12px;
    border-radius: 50%; background: var(--paw);
  }
  .features .note { display: block; font-size: 11px; line-height: 13px; margin-top: 1px; }
  .contact { position: absolute; left: 640px; top: 280px; width: 472px; text-align: center; font-weight: 700; }
  .contact-line { font-size: 18px; line-height: 26px; letter-spacing: 0.5px; }
  .contact-phone { display: flex; align-items: center; justify-content: center; gap: 10px; margin-top: 10px; font-size: 34px; font-weight: 700; }
  .contact-phone svg { width: 36px; height: 36px; }
  .brand-badge {
    position: absolute; left: -60px; top: 225px; width: 330px; height: 330px;
    border-radius: 50%; background: var(--white); border: 8px solid var(--ring);
  }
  .brand-name {
    position: absolute; left: 16px; top: 300px; width: 230px; text-align: center;
    font-size: 24px; font-weight: 900; line-height: 28px; color: var(--ink); letter-spacing: 0.5px;
  }
  .offer-band { position: absolute; left: 0; top: 390px; width: 1200px; height: 165px; background: var(--band); }
  .offer {
    position: absolute; top: 21px; width: 366px; height: 121px; display: flex; align-items: center; justify-content: center;
    text-align: center; color: var(--white); font-weight: 700; font-size: 32px; line-height: 36px;
  }
  .offer sup { font-size: 24px; position: relative; top: -6px; margin-left: 2px; }
  .offer-daycare { left: 16px; background: var(--offer-mid); }
  .offer-bath { left: 417px; background: var(--offer-deep); }
  .offer-groom { left: 818px; background: var(--offer-dark); }
  .fine-print {
    position: absolute; left: 0; top: 555px; width: 1200px; height: 73px; background: var(--footer);
    color: var(--white); font-size: 22px; letter-spacing: 0.3px; display: flex; align-items: center; justify-content: center;
  }
</style>
</head>
<body>
<div class="ad">
  <div class="hero-photo" role="img" aria-label="Photo of three dogs resting together on a wooden floor"></div>

  <svg class="panel-shape" viewBox="0 0 1200 390" aria-hidden="true">
    <defs>
      <linearGradient id="panelFill" x1="0" y1="0" x2="1" y2="1">
        <stop offset="0" style="stop-color: var(--panel-1)"/>
        <stop offset="1" style="stop-color: var(--panel-2)"/>
      </linearGradient>
      <linearGradient id="stripFill" x1="0" y1="0" x2="1" y2="0">
        <stop offset="0" style="stop-color: var(--strip-1); stop-opacity: 0"/>
        <stop offset="0.12" style="stop-color: var(--strip-1)"/>
        <stop offset="1" style="stop-color: var(--strip-2)"/>
      </linearGradient>
    </defs>
    <path d="M488 0 H1200 V272 H612 C590 180 540 80 488 0 Z" fill="url(#panelFill)"/>
    <rect x="600" y="268" width="600" height="122" fill="url(#stripFill)"/>
  </svg>

  <div class="headline">
    <div class="headline-kicker">NOT YOUR TYPICAL</div>
    <div class="headline-main">DOG DAY CARE</div>
  </div>

  <ul class="features">
    <li>SAFE, OPEN-PLAY DAY CARE</li>
    <li>EXERCISE &amp; EDUCATION</li>
    <li>FUN FILLED DAYS WITH THEIR BFFF<span class="note">(BEST FURRY FRIEND FOREVER)</span></li>
    <li>LIVE PLAYROOM WEBCAMS</li>
  </ul>

  <div class="contact">
    <div class="contact-line">Bright Meadow Club</div>
    <div class="contact-line">418 Orchard Row Millbrook, IA, 50999</div>
    <div class="contact-phone">
      <svg viewBox="0 0 34 34" aria-hidden="true">
        <circle cx="17" cy="17" r="15" fill="none" style="stroke: var(--paw)" stroke-width="2.5"/>
        <path d="M12 9 l4 0 l1 5 l-2.5 1.5 c1 2.5 2.5 4 5 5 l1.5 -2.5 l5 1 l0 4 c-8 1 -15 -6 -14 -14 z" style="fill: var(--paw)"/>
      </svg>
      <span>555-201-7734</span>
    </div>
  </div>

  <div class="brand-badge"></div>
  <div class="brand-name">BRIGHT MEADOW CLUB</div>

  <div class="offer-band">
    <div class="offer offer-daycare"><span>FREE FIRST DAY<sup>*</sup><br>OF DAY CARE</span></div>
    <div class="offer offer-bath"><span>ONE FREE BATH<sup>*</sup></span></div>
    <div class="offer offer-groom"><span>$20 OFF<sup>*</sup><br>FIRST GROOM</span></div>
  </div>

  <div class="fine-print">*&nbsp; Advanced reservations required. Call to schedule your appointment. Use by 8/31/2020.</div>
</div>
</body>
</html>
```